We need letterhead, Business Cards, and envelops designed. We have attached a design of our logo and a sample of letterhead idea that was started but never perfected, it is only an idea for the letterhead if you can design something better we may love that also we are open to change.
We want a design that looks professional in style. we are a non profit trade association in the construction industry. the green color in the attached design represent green building, and we like that. also if you just want to enhance the letterhead sample that we attached that would be fine also.
Thanks and good luck
also the name that should show on the first business cards should be Merwin Habsfield, Director are web address is www.tqvmp.org

```html
<!DOCTYPE html>
<html lang="en">
<head>
<meta charset="utf-8">
<title>Envelope – Harbor State Builders Alliance</title>
<link rel="stylesheet" href="https://fonts.googleapis.com/css2?family=Questrial&display=swap">
<style>
  :root {
    --flap-green: #8cff2a;
    --paper: #ffffff;
    --edge: #b5b5b5;
    --ink: #111111;
    --deco-green: #c4e3bb;
    --backdrop: #ffffff;
  }
  * { margin: 0; padding: 0; box-sizing: border-box; }
  html, body {
    width: 1200px;
    height: 849px;
    overflow: hidden;
    background: var(--backdrop);
  }
  .canvas {
    position: relative;
    width: 1200px;
    height: 849px;
    font-family: "Questrial", "Century Gothic", sans-serif;
    color: var(--ink);
  }
  .envelope-shape {
    position: absolute;
    left: 0;
    top: 0;
  }
  .flap-return {
    position: absolute;
    left: 124px;
    top: 103px;
    width: 944px;
    height: 202px;
    display: flex;
    flex-direction: column;
    align-items: center;
    justify-content: center;
    gap: 9px;
    transform: rotate(180deg);
    font-size: 15px;
    line-height: 19px;
    letter-spacing: 0.2px;
  }
  .brand {
    position: absolute;
    left: 197px;
    top: 500px;
    display: flex;
    align-items: center;
    gap: 12px;
  }
  .brand-mark {
    width: 22px;
    height: 22px;
    background: var(--flap-green);
  }
  .brand-name {
    font-size: 27px;
    line-height: 32px;
    color: var(--ink);
  }
  .corner-decoration {
    position: absolute;
    left: 759px;
    top: 487px;
    width: 281px;
    height: 255px;
    background: linear-gradient(180deg, #d6edd0 0%, var(--deco-green) 100%);
  }
</style>
</head>
<body>
<main class="canvas">
  <svg class="envelope-shape" width="1200" height="849" viewBox="0 0 1200 849" aria-hidden="true">
    <path class="envelope-flap" fill="var(--flap-green)"
      d="M124 305 L158 150 Q172 103 240 103 L958 103 Q1030 103 1044 150 L1068 305 Z"/>
    <rect class="envelope-body" x="124.5" y="305.5" width="943" height="436" fill="var(--paper)" stroke="var(--edge)" stroke-width="1"/>
    <rect class="flap-tab" x="124" y="305" width="196" height="24" fill="var(--flap-green)"/>
  </svg>

  <div class="flap-return">
    <p class="return-address">2140 Larkfield Avenue, Brookmont, CO 80455</p>
    <p class="return-phone">Tel: (555) 318-2047</p>
    <p class="return-email">Email: info@tqvmp.org</p>
    <p class="return-web">www.tqvmp.org</p>
  </div>

  <div class="brand">
    <span class="brand-mark"></span>
    <span class="brand-name">Harbor State Builders Alliance</span>
  </div>

  <div class="corner-decoration" role="img" aria-label="Faint pale green building silhouette decoration"></div>
</main>
</body>
</html>
```